Property Management Firm Introduces New Programs

4 pages, 5.5 x 8.5 finished size, 4-color
We are introducing two new programs: Financial Management and Q-Steward. These programs are more affordable than full-service management. The brochure should come across as professional but not too glossy to give the impression of affordability coupled with stability and reliability. That said, we like to have a little fun with what we do--or it's not worth doing.

Target Market(s)

self-managed HOA and condo association

Industry/Entity Type

Real Estate

Other font styles liked:
• Trocchi, Activ Grotesk

Requirements
Must have
• Easy to read
• Our corporate fonts are Trocchi and Aktiv Grotesk
• Let me know if you need me to upload those fonts.
• LOGO Colors
• Red / Green / Blue
• Cyan 27 84 74
• Magenta 98 25 75
• Yellow 81 96 3
• Black 49 28 85
Nice to have
• The content is submitted in a rough design format to give you an idea of what we are looking for. I've attached the photos used in the design. Am open to the idea of different photos. This has a tight deadline so trying to give as much as possible

```html
<!DOCTYPE html>
<html lang="en">
<head>
<meta charset="utf-8">
<title>Q-Steward Program</title>
<link rel="stylesheet" href="https://fonts.googleapis.com/css2?family=Roboto:wght@700&family=Trocchi&display=swap">
<style>
  :root {
    --frame: #3b3b3d;
    --paper: #ffffff;
    --paper-shade: #e4e4e6;
    --brand-red: #7b1522;
    --ink: #1c1c1c;
    --photo-light: #d9dde3;
    --photo-blue: #2f6fb8;
    --gold: #e2b22c;
    --gold-deep: #b07d12;
  }
  * { box-sizing: border-box; margin: 0; padding: 0; }
  html, body { width: 800px; height: 1200px; overflow: hidden; }
  body { background: var(--frame); position: relative; font-family: "Trocchi", serif; color: var(--ink); }

  .page {
    position: absolute; left: 35px; top: 46px; width: 722px; height: 1114px;
    background: linear-gradient(90deg, var(--paper-shade) 0%, var(--paper) 22%, var(--paper) 100%);
    overflow: hidden;
  }
  .hero-photo {
    position: absolute; left: 0; top: 0; width: 722px; height: 292px;
    background: linear-gradient(100deg, var(--photo-light) 0%, #c9ced6 40%, #5b86bd 62%, var(--photo-blue) 78%, #c7ccd3 100%);
  }
  .hero-rule { position: absolute; left: 0; top: 292px; width: 722px; height: 3px; background: var(--brand-red); }

  .program-title {
    position: absolute; left: 0; top: 312px; width: 722px; text-align: center;
    font-family: "Roboto", sans-serif; font-weight: 700; font-size: 45px; color: var(--brand-red); letter-spacing: -0.5px;
  }

  .mouse-art {
    position: absolute; left: 549px; top: 376px; width: 104px; height: 78px; border-radius: 45%;
    background: linear-gradient(135deg, #c9252c 0%, #a9a9ad 70%, #d8d8da 100%);
  }

  .content { position: absolute; left: 33px; top: 396px; width: 655px; font-size: 16.6px; line-height: 21.2px; }
  .section-heading { font-size: 28.5px; line-height: 34px; color: var(--brand-red); font-weight: 400; margin-bottom: 2px; }
  .section-heading.second { margin-top: 2px; }
  .content p { margin: 0; }
  .content u { text-decoration: underline; }

  .feature-list { list-style: none; margin-left: 66px; }
  .feature-list li { position: relative; }
  .feature-list li::before {
    content: ""; position: absolute; left: -24px; top: 6px;
    border-left: 6px solid var(--brand-red); border-top: 4.5px solid transparent; border-bottom: 4.5px solid transparent;
  }
  .feature-list li.list-label::before { display: none; }

  .support-badge { position: absolute; left: 547px; top: 943px; width: 138px; height: 138px; }
</style>
</head>
<body>
  <main class="page">
    <div class="hero-photo" role="img" aria-label="Person in a blue hoodie typing on a laptop, with white finance icons floating above"></div>
    <div class="hero-rule"></div>

    <h1 class="program-title">Q-STEWARD</h1>

    <div class="mouse-art" role="img" aria-label="Red and grey computer mouse illustration"></div>

    <section class="content">
      <h2 class="section-heading">What do you get?</h2>
      <p>All the financial services and options, <u>PLUS</u> the power<br>
      of our robust management software to help with all your administrative needs. With our Q-Steward program, you or your staff will manage the web portal. We can turn functions on or off to suit your needs.</p>
      <p>Some of the administrative functions you will have available include:</p>
      <ul class="feature-list">
        <li>Templated Board meeting agendas and minutes</li>
        <li>Documents storage</li>
        <li>Managing maintenance requests</li>
        <li>Conducting covenants inspections and issuing violation notices</li>
        <li>Managing the architectural change request process</li>
        <li>Issuing mass communications to your residents via U.S. Mail, email, pop-up messages or texts</li>
        <li>Managing clubhouse rental schedules</li>
        <li>An QSP coordinator to help with questions and training for your Board and homeowners</li>
      </ul>
      <p>When these functions are activated, your residents will enjoy added convenience as well as open and interactive communications with your Board, which leads to trust, confidence and, ultimately, a more engaged community.</p>

      <h2 class="section-heading second">What else can you get?</h2>
      <p>You may qualify for hourly consulting and a-la-carte services for an additional fee, such as:</p>
      <ul class="feature-list">
        <li>Issuance of resale disclosure packages</li>
        <li>Budget assistance</li>
        <li>Credit reporting</li>
        <li class="list-label">Q-STEWARD ONLY:</li>
        <li>Covenants enforcement</li>
        <li>Annual meeting administration</li>
        <li>Project management</li>
        <li>Insurance claims management</li>
      </ul>
    </section>

    <svg class="support-badge" viewBox="0 0 138 138" role="img" aria-label="Support badge">
      <defs>
        <radialGradient id="badgeCore" cx="45%" cy="35%" r="65%">
          <stop offset="0" stop-color="#b42a32"/>
          <stop offset="1" stop-color="#5e0d14"/>
        </radialGradient>
        <linearGradient id="badgeRing" x1="0" y1="0" x2="0" y2="1">
          <stop offset="0" stop-color="#f7d35a"/>
          <stop offset="1" stop-color="#b07d12"/>
        </linearGradient>
      </defs>
      <circle cx="69" cy="69" r="68" fill="#e6e6e6"/>
      <circle cx="69" cy="69" r="62" fill="url(#badgeRing)"/>
      <circle cx="69" cy="69" r="53" fill="url(#badgeCore)"/>
    </svg>
  </main>
</body>
</html>
```